Buisness card

**Front Side:**

**[Your Company Logo]**
**Steadfast Upkeep Industrial**
*Keeping Your Equipment Running Smoothly*

**Contact Information:**
- **Name:** [darren Whitlow
- **Title:** [owner
- **Phone:** [8025196047
- **Email:** darren@sukrn.com

**Back Side:**

**Services Offered:**
- Routine Inspections
- Equipment Maintenance
- Emergency Repairs
- Consultation Services
- New installs
Tag line
Be proactive not reactive

```html
<!DOCTYPE html>
<html lang="en">
<head>
<meta charset="utf-8">
<title>Steadfast Upkeep Industrial – Business Card</title>
<link rel="stylesheet" href="https://fonts.googleapis.com/css2?family=Roboto:wght@400;500;700&family=Montserrat:wght@700&family=Tinos&display=swap">
<style>
  :root {
    --page-bg: #1c1c1e;
    --card-white: #ffffff;
    --navy: #0b2a6b;
    --navy-deep: #07215c;
    --teal-glow: #0a7596;
    --brand-blue: #0d3f8f;
    --name-blue: #0d4f8b;
    --cyan: #00c8f5;
    --accent-red: #e8343c;
    --ink: #1a1a1a;
    --ink-soft: #333333;
  }
  * { box-sizing: border-box; margin: 0; padding: 0; }
  html, body { width: 1200px; height: 1059px; overflow: hidden; }
  body {
    background: var(--page-bg);
    font-family: "Roboto", Arial, sans-serif;
    position: relative;
  }
  .card {
    position: absolute;
    left: 254px;
    width: 698px;
    height: 398px;
    background: var(--card-white);
    border-radius: 28px;
    overflow: hidden;
  }
  .card--front { top: 97px; }
  .card--back { top: 552px; }

  /* Front */
  .brand-name {
    position: absolute;
    font-family: "Roboto", Arial, sans-serif;
    font-weight: 700;
    color: var(--brand-blue);
    line-height: 1.05;
  }
  .card--front .brand-name { left: 28px; top: 42px; font-size: 34px; }
  .brand-mark {
    position: absolute;
    border-radius: 50%;
    background: var(--navy);
  }
  .card--front .brand-mark { left: 446px; top: 104px; width: 178px; height: 178px; }

  .side-tab {
    position: absolute; left: 0; top: 174px;
    width: 8px; height: 52px;
    background: linear-gradient(90deg, var(--navy-deep), var(--brand-blue));
  }
  .person-name {
    position: absolute; left: 30px; top: 164px;
    font-weight: 500; font-size: 28px; color: var(--name-blue);
    letter-spacing: -0.2px;
  }
  .person-title {
    position: absolute; left: 28px; top: 205px;
    font-family: "Tinos", "Times New Roman", serif;
    font-size: 22px; color: var(--ink);
  }
  .contact {
    position: absolute; left: 26px;
    display: flex; align-items: center; gap: 12px;
    font-size: 19px; color: var(--ink-soft); letter-spacing: 0.3px;
  }
  .contact--phone { top: 250px; }
  .contact--email { top: 285px; }
  .contact svg { width: 22px; height: 22px; flex: none; }

  .rule-red {
    position: absolute; left: 0; right: 0; top: 341px;
    height: 4px; background: var(--accent-red);
  }
  .front-band {
    position: absolute; left: 0; right: 0; top: 347px; bottom: 0;
    background: radial-gradient(ellipse at 50% 20%, var(--teal-glow) 0%, var(--navy) 55%, var(--navy-deep) 100%);
    display: flex; align-items: center; justify-content: center;
    padding-bottom: 4px;
  }
  .front-band__text {
    font-family: "Montserrat", Arial, sans-serif;
    font-weight: 700; font-size: 25px; color: #fff;
  }

  /* Back */
  .card--back .brand-mark { left: 104px; top: 43px; width: 100px; height: 100px; }
  .card--back .brand-name { left: 236px; top: 54px; font-size: 34px; }

  .services {
    position: absolute; left: 0; right: 0; top: 177px; height: 162px;
    background: radial-gradient(ellipse at 50% 0%, var(--teal-glow) 0%, var(--navy) 50%, var(--navy-deep) 100%);
    color: #fff; text-align: center;
  }
  .services__heading {
    margin-top: 31px;
    font-weight: 700; font-size: 26px; letter-spacing: 7px;
  }
  .services__list {
    list-style: none; margin-top: 12px;
    font-size: 20px; line-height: 31px;
  }
  .services__list li { display: inline; }
  .services__list li::before { content: "• "; }
  .tagline-band {
    position: absolute; left: 0; right: 0; top: 338px; height: 43px;
    background: var(--cyan);
    display: flex; align-items: center; justify-content: center;
    font-weight: 700; font-size: 23px; color: #fff;
  }
  .back-foot {
    position: absolute; left: 0; right: 0; top: 381px; bottom: 0;
    background: var(--navy);
  }
</style>
</head>
<body>
  <section class="card card--front">
    <div class="brand-name">Steadfast Upkeep<br>Industrial</div>
    <div class="brand-mark"></div>

    <div class="side-tab"></div>
    <h1 class="person-name">darren Whitlow</h1>
    <p class="person-title">Owner</p>

    <p class="contact contact--phone">
      <svg viewBox="0 0 24 24" aria-hidden="true"><path fill="var(--brand-blue)" d="M6.6 10.8c1.4 2.8 3.8 5.1 6.6 6.6l2.2-2.2c.3-.3.7-.4 1-.2 1.1.4 2.3.6 3.6.6.6 0 1 .4 1 1V20c0 .6-.4 1-1 1C10.6 21 3 13.4 3 4c0-.6.4-1 1-1h3.5c.6 0 1 .4 1 1 0 1.3.2 2.5.6 3.6.1.3 0 .7-.2 1z"/></svg>
      8025196047
    </p>
    <p class="contact contact--email">
      <svg viewBox="0 0 24 24" aria-hidden="true"><rect x="2" y="5" width="20" height="14" fill="var(--brand-blue)"/><path d="M2 5l10 8 10-8" fill="none" stroke="#fff" stroke-width="1.8"/></svg>
      darren@sukrn.com
    </p>

    <div class="rule-red"></div>
    <div class="front-band"><span class="front-band__text">Keeping Your Equipment Running Smoothly</span></div>
  </section>

  <section class="card card--back">
    <div class="brand-mark"></div>
    <div class="brand-name">Steadfast Upkeep<br>Industrial</div>

    <div class="services">
      <h2 class="services__heading">SERVICES OFFERED</h2>
      <ul class="services__list">
        <li>Routine Inspections</li> <li>Equipment Maintenance</li><br>
        <li>Emergency Repairs</li> <li>Consultation Services</li> <li>New installs</li>
      </ul>
    </div>
    <div class="tagline-band">Be proactive not reactive</div>
    <div class="back-foot"></div>
  </section>
</body>
</html>
```